Motivational Poster Design Project

I would like to create a poster with some of my favorite quotes to hang in my office.

Industry/Entity Type

Quotes

Requirements
Must have
• The poster will be 24" high x 36" long and printed on canvas, so the image you create needs to have a resolution of at least 2700 x 3900.

The poster must contain the following quotes:

“Your beliefs become your thoughts,
Your thoughts become your words,
Your words become your actions,
Your actions become your habits,
Your habits become your values,
Your values become your destiny.”
-Varuna Pellath

"Winners practice until they get it right. Champions practice until they can’t get it wrong!"
-Unknown

"Style is the perfection of a point of view."
-Conrad Whitlowe

"My interest in life comes from setting myself huge, apparently unachieveable challenges and trying to rise above them."
-Sir Oswin Talbrook

"Problems cannot be solved by the same level of thinking that created them."
-Gustav Morrendel

"People think focus means saying yes to the thing you've got to focus on. But that's not what it means at all. It means saying no to the hundred other good ideas that there are. You have to pick carefully."
-Dale Parrick

"Think like a man of action and act like a man of thought."
-Lucien Marvaud
Nice to have
• It would be nice to have an image of each person who is being quoted (if known) along with the quote that is attributable to them.

```html
<!DOCTYPE html>
<html lang="en">
<head>
<meta charset="utf-8">
<title>Favorite Quotes Poster</title>
<link rel="stylesheet" href="https://fonts.googleapis.com/css2?family=Courgette&family=Open+Sans:wght@600&display=swap">
<style>
  :root {
    --page-bg: #ffffff;
    --poster-top: #f1f1f1;
    --poster-bottom: #a1a1a1;
    --quote-ink: #1e1e1e;
    --author-blue: #2b8fd9;
  }
  html, body {
    margin: 0;
    padding: 0;
    overflow: hidden;
    background: var(--page-bg);
  }
  .canvas {
    position: relative;
    width: 1200px;
    height: 1000px;
    overflow: hidden;
    background: var(--page-bg);
  }
  .poster {
    position: absolute;
    left: 267px;
    top: 0;
    width: 693px;
    height: 1000px;
    background: linear-gradient(to bottom, var(--poster-top), var(--poster-bottom));
  }
  .line {
    position: absolute;
    height: 30px;
    line-height: 30px;
    white-space: nowrap;
    font-family: "Courgette", cursive;
    color: var(--quote-ink);
    font-size: 22px;
  }
  .line--small { font-size: 20px; }
  .line--large { font-size: 23px; }
  .line--condensed {
    font-size: 24px;
    transform: scaleX(0.74);
    transform-origin: left center;
  }
  .author {
    position: absolute;
    left: 453px;
    height: 30px;
    line-height: 30px;
    white-space: nowrap;
    font-family: "Open Sans", sans-serif;
    font-weight: 600;
    font-size: 22px;
    color: var(--author-blue);
  }
</style>
</head>
<body>
<div class="canvas">
  <main class="poster">
    <section class="quote quote--beliefs">
      <div class="line line--small" style="top:25px;left:43px">“Your beliefs become your thoughts,</div>
      <div class="line line--small" style="top:54px;left:43px">Your thoughts become your words,</div>
      <div class="line line--small" style="top:82px;left:43px">Your words become your actions,</div>
      <div class="line line--small" style="top:111px;left:43px">Your actions become your habits,</div>
      <div class="line line--small" style="top:139px;left:43px">Your habits become your values,</div>
      <div class="line line--small" style="top:168px;left:43px">Your values become your destiny.”</div>
      <div class="author" style="top:197px">-Varuna Pellath</div>
    </section>

    <section class="quote quote--winners">
      <div class="line line--large" style="top:241px;left:46px">"Winners practice until they get it right.</div>
      <div class="line line--large" style="top:276px;left:7px">Champions practice until they can’t get it wrong!"</div>
      <div class="author" style="top:309px">-Unknown</div>
    </section>

    <section class="quote quote--style">
      <div class="line line--large" style="top:351px;left:15px">"Style is the perfection of a point of view."</div>
      <div class="author" style="top:382px">-Conrad Whitlowe</div>
    </section>

    <section class="quote quote--challenges">
      <div class="line" style="top:426px;left:13px">"My interest in life comes from setting myself huge,</div>
      <div class="line" style="top:462px;left:88px">apparently unachieveable challenges</div>
      <div class="line" style="top:496px;left:118px">and trying to rise above them."</div>
      <div class="author" style="top:524px">-Sir Oswin Talbrook</div>
    </section>

    <section class="quote quote--problems">
      <div class="line line--condensed" style="top:578px;left:5px">"Problems cannot be solved by the same level of thinking that created them."</div>
      <div class="author" style="top:615px">-Gustav Morrendel</div>
    </section>

    <section class="quote quote--focus">
      <div class="line" style="top:669px;left:10px">"People think focus means saying yes to the thing you've got</div>
      <div class="line" style="top:704px;left:63px">to focus on. But that's not what it means at all.</div>
      <div class="line" style="top:738px;left:8px">It means saying no to the hundred other good ideas that there</div>
      <div class="line" style="top:773px;left:145px">are. You have to pick carefully."</div>
      <div class="author" style="top:818px">-Dale Parrick</div>
    </section>

    <section class="quote quote--thought">
      <div class="line" style="top:869px;left:10px">"Think like a man of action and act like a man of thought."</div>
      <div class="author" style="top:910px">-Lucien Marvaud</div>
    </section>
  </main>
</div>
</body>
</html>
```